Bill board design For Marlowe’s Construction

Billboard Design Request
Please design the billboard to match the branding, colors, and overall feel of our website: Marlowe's Construction Website
MARLOWE’S CONSTRUCTION
CONCRETE BUILT FOR GENERATIONS
⭐ 5-Star Rated on Zorvix
Please Include:
* All three attached project photos
* Company logo(s)
* Phone Number: 555-214-7630
* Website: MarlowesConstruction.example
* Zorvix logo with 5-star rating graphic
* Chatterly logo
* Pixtoria logo
Service Area:
Kalamazoo • Battle Creek • Coldwater • Grand Rapids
Please arrange the photos and layout in whatever way creates the strongest visual impact and readability from the road. The company name, headline, phone number, and website should be highly visible at highway speeds.
The overall appearance should be clean, professional, premium, and consistent with our website branding while highlighting our reputation, craftsmanship, and quality concrete work.
People Driving By
Concrete Construction

```html
<!DOCTYPE html>
<html lang="en">
<head>
<meta charset="utf-8">
<title>Marlowe’s Construction Billboard</title>
<link rel="stylesheet" href="https://fonts.googleapis.com/css2?family=Bebas+Neue&family=Poppins:wght@500;600;700;800&display=swap">
<style>
  :root {
    --page-bg: #dcd3d0;
    --board-black: #0b0b0c;
    --board-dark: #1a1a1c;
    --brand-blue: #1c94e4;
    --white: #ffffff;
    --photo-warm: #8a6a48;
    --photo-green: #5d6e3e;
    --photo-concrete: #c9c3b8;
    --photo-brick: #a8522e;
    --star-gold: #f7c21a;
    --social-blue: #2566e8;
    --social-pink: #e23b8a;
    --grey-text: #b8b8b8;
  }
  * { margin: 0; padding: 0; box-sizing: border-box; }
  html, body { width: 890px; height: 1200px; overflow: hidden; }
  body {
    background: var(--page-bg);
    font-family: "Poppins", sans-serif;
    position: relative;
  }
  .billboard {
    position: absolute;
    left: 35px; top: 395px;
    width: 820px; height: 410px;
    background: radial-gradient(ellipse at 40% 30%, var(--board-dark), var(--board-black) 70%);
    box-shadow: 0 10px 18px rgba(0,0,0,0.35);
    color: var(--white);
  }
  .brand-mark {
    position: absolute; left: 27px; top: 40px; width: 196px;
    text-align: center; color: var(--brand-blue); font-weight: 600;
  }
  .brand-mark__square {
    display: block; width: 46px; height: 46px; margin: 0 auto 10px;
    background: var(--brand-blue); border-radius: 4px;
  }
  .brand-mark__name { font-size: 27px; line-height: 1; letter-spacing: 0.5px; }
  .brand-mark__sub { font-size: 8.5px; letter-spacing: 3.6px; margin-top: 4px; }
  .project-photo {
    position: absolute; top: 39px; width: 177px; height: 119px;
    border-radius: 9px; border: 1.5px solid var(--white);
  }
  .project-photo--crew { left: 240px; background: linear-gradient(160deg, var(--photo-green), var(--photo-warm) 60%, #2a2622); }
  .project-photo--garage { left: 425px; background: linear-gradient(180deg, var(--photo-green) 0%, #8c6e5a 40%, var(--photo-concrete) 60%, #e6e1d8); }
  .project-photo--walkway { left: 611px; background: linear-gradient(180deg, #7b6a52 0%, var(--photo-green) 35%, var(--photo-brick) 60%, #c46e42); }
  .tagline-band {
    position: absolute; left: 30px; top: 179px; width: 756px; height: 47px;
    background: var(--brand-blue); border-radius: 9px;
    display: flex; align-items: center; justify-content: center;
    font-weight: 700; font-size: 22px; letter-spacing: 7.4px; padding-left: 7px;
  }
  .company-name {
    position: absolute; left: 31px; top: 238px;
    font-family: "Bebas Neue", sans-serif; font-size: 82px; line-height: 66px;
  }
  .company-name__first { color: var(--brand-blue); display: block; }
  .company-name__second { color: var(--white); display: block; letter-spacing: -0.5px; }
  .contact-line { position: absolute; left: 432px; display: flex; align-items: center; }
  .contact-line--phone { top: 238px; font-weight: 700; font-size: 44px; line-height: 48px; letter-spacing: 0.5px; }
  .contact-line--web { top: 286px; font-weight: 600; font-size: 20px; line-height: 28px; }
  .contact-icon { flex: none; margin-right: 9px; }
  .contact-line--web .contact-icon { margin-left: 3px; margin-right: 10px; }
  .review-badge { position: absolute; left: 467px; top: 319px; width: 140px; }
  .review-badge__name { font-weight: 600; font-size: 40px; line-height: 44px; color: var(--brand-blue); }
  .review-badge__label { font-size: 7.5px; font-weight: 500; margin-left: 30px; line-height: 9px; }
  .review-badge__stars { font-size: 7.5px; color: var(--star-gold); margin-left: 30px; line-height: 10px; }
  .review-text {
    position: absolute; left: 618px; top: 333px;
    font-weight: 600; font-size: 13.5px; line-height: 18px;
  }
  .social-list { position: absolute; left: 712px; top: 338px; list-style: none; }
  .social-item { display: flex; align-items: center; font-weight: 600; font-size: 11px; height: 18px; margin-bottom: 4px; }
  .social-item__square { width: 14px; height: 14px; border-radius: 3px; margin-right: 5px; }
  .social-item--chatterly .social-item__square { background: var(--social-blue); }
  .social-item--pixtoria .social-item__square { background: var(--social-pink); }
</style>
</head>
<body>
  <main class="billboard">
    <div class="brand-mark">
      <span class="brand-mark__square"></span>
      <div class="brand-mark__name">MARLOWE’S</div>
      <div class="brand-mark__sub">CONSTRUCTION L.L.C</div>
    </div>

    <div class="project-photo project-photo--crew" role="img" aria-label="Crew member pouring concrete from a truck chute in a residential yard"></div>
    <div class="project-photo project-photo--garage" role="img" aria-label="New concrete driveway leading to a detached garage"></div>
    <div class="project-photo project-photo--walkway" role="img" aria-label="Stamped terracotta concrete walkway leading to a house"></div>

    <div class="tagline-band">CONCRETE BUILT FOR GENERATIONS</div>

    <h1 class="company-name">
      <span class="company-name__first">MARLOWE’S</span>
      <span class="company-name__second">CONSTRUCTION</span>
    </h1>

    <div class="contact-line contact-line--phone">
      <svg class="contact-icon" width="28" height="28" viewBox="0 0 28 28" aria-hidden="true">
        <circle cx="14" cy="14" r="13" fill="var(--brand-blue)" stroke="#fff" stroke-width="1.5"/>
        <path d="M9.5 7.5c.8-.6 1.8-.4 2.2.4l1 2c.3.7.1 1.4-.5 1.8l-.8.6c.6 1.6 1.8 2.9 3.3 3.6l.6-.8c.5-.6 1.2-.7 1.8-.4l2 1c.8.4 1 1.4.4 2.2l-.8 1c-.7.8-1.9 1.1-2.9.6-3.3-1.5-5.9-4.2-7.3-7.5-.4-1 0-2.1.7-2.8z" fill="#fff"/>
      </svg>
      555-214-7630
    </div>

    <div class="contact-line contact-line--web">
      <svg class="contact-icon" width="22" height="22" viewBox="0 0 22 22" aria-hidden="true">
        <circle cx="11" cy="11" r="10" fill="var(--brand-blue)" stroke="#fff" stroke-width="1.5"/>
        <circle cx="11" cy="11" r="5.5" fill="none" stroke="#fff" stroke-width="1.2"/>
        <ellipse cx="11" cy="11" rx="2.4" ry="5.5" fill="none" stroke="#fff" stroke-width="1"/>
        <line x1="5.5" y1="11" x2="16.5" y2="11" stroke="#fff" stroke-width="1"/>
      </svg>
      MarlowesConstruction.example
    </div>

    <div class="review-badge">
      <div class="review-badge__name">Zorvix</div>
      <div class="review-badge__label">REVIEWS</div>
      <div class="review-badge__stars">5.0 ★★★★★</div>
    </div>

    <div class="review-text">5-Star<br>Rated on<br>Zorvix</div>

    <ul class="social-list">
      <li class="social-item social-item--chatterly"><span class="social-item__square"></span>Chatterly</li>
      <li class="social-item social-item--pixtoria"><span class="social-item__square"></span>Pixtoria</li>
    </ul>
  </main>
</body>
</html>
```